Group Fitness Bootcamp

We are a new medical fitness company and we are starting a bootcamp fitness program. We also provide diet programs, metabolic and physiological testing. We would like to use our logo colors and the final design should have a clean look

```html
<!DOCTYPE html>
<html lang="en">
<head>
<meta charset="utf-8">
<title>Aura Wellness – Boot-Camp Fitness and Boxing</title>
<link href="https://fonts.googleapis.com/css2?family=Oswald:wght@400;500;600&family=Lato:ital,wght@0,400;0,700;1,400;1,700&display=swap" rel="stylesheet">
<style>
  :root{
    --ink:#2a2a2c;
    --ink-soft:#3b3b3e;
    --paper:#f4f3f1;
    --white:#ffffff;
    --sand:#d8c5aa;
    --sand-dark:#bfa988;
    --amber:#d49a45;
    --stone:#7f7873;
    --silver:#c9c6c2;
  }
  *{box-sizing:border-box;margin:0;padding:0}
  html,body{width:902px;height:1200px;overflow:hidden;background:var(--paper)}
  .flyer{position:relative;width:902px;height:1200px;overflow:hidden;background:var(--paper);font-family:'Lato',sans-serif;color:var(--ink)}
  .backdrop{position:absolute;inset:0}
  .hero-photo{position:absolute;left:0;top:60px;width:902px;height:720px;background:radial-gradient(ellipse at 25% 55%,#6a5a50 0%,#3a3533 40%,#1d1c1d 80%)}
  .brand{position:absolute;left:108px;top:62px;display:flex;align-items:center;gap:14px}
  .brand-dot{width:34px;height:34px;border-radius:50%;background:var(--stone)}
  .brand-name{font-family:'Lato',sans-serif;font-weight:400;font-size:40px;color:var(--stone);letter-spacing:1px}
  .social{position:absolute;left:495px;top:66px;display:flex;align-items:center;gap:8px}
  .social-label{font-style:italic;font-weight:700;font-size:14px;color:var(--stone);margin-right:8px}
  .social-square{width:28px;height:28px;border-radius:5px;background:var(--ink-soft)}
  .headline{position:absolute;left:466px;top:220px;width:396px;text-align:center}
  .headline-main{font-family:'Oswald',sans-serif;font-weight:600;font-size:76px;line-height:1;color:var(--white);white-space:nowrap}
  .headline-tag{display:inline-block;margin-top:10px;background:var(--sand);padding:4px 16px;font-family:'Oswald',sans-serif;font-weight:500;font-size:40px;line-height:1.2;color:var(--ink);white-space:nowrap}
  .coach{position:absolute;left:466px;top:398px;width:396px;text-align:center;font-family:'Lato',sans-serif;font-weight:700;font-size:25px;line-height:1.28;color:var(--white);text-transform:uppercase;letter-spacing:.5px;white-space:nowrap}
  .coach-nick{color:var(--sand)}
  .intro{position:absolute;left:519px;top:536px;width:290px;text-align:center;font-size:14.5px;line-height:1.3;color:var(--white)}
  .launch{position:absolute;left:60px;top:714px;width:460px;height:80px}
  .launch-text{position:absolute;left:44px;top:10px;font-family:'Oswald',sans-serif;font-weight:500;font-size:44px;line-height:1.2;color:var(--ink);white-space:nowrap}
  .launch-month{color:var(--amber)}
  .class-photo{position:absolute;left:522px;top:618px;width:264px;height:264px;border-radius:50%;border:7px solid var(--white);background:linear-gradient(160deg,#b9a898 0%,#6e625a 55%,#2e2b2a 100%);box-shadow:0 4px 10px rgba(0,0,0,.25)}
  .benefits{position:absolute;left:44px;top:852px;width:480px;list-style:none}
  .benefits li{position:relative;padding-left:30px;margin-bottom:20px;font-style:italic;font-size:14.5px;line-height:1.3;color:var(--ink)}
  .benefits svg{position:absolute;left:0;top:3px}
  .pricing{position:absolute;left:618px;top:918px;width:196px;text-align:center}
  .plan{margin-bottom:14px}
  .plan-label{display:block;height:28px;line-height:28px;font-size:15px;color:var(--white);background:var(--ink);clip-path:polygon(0 0,100% 0,90% 100%,10% 100%)}
  .plan-price{display:flex;justify-content:center;align-items:center;gap:8px;margin-top:6px}
  .plan-amount{font-family:'Oswald',sans-serif;font-weight:500;font-size:34px;line-height:1;color:var(--ink)}
  .plan-unit{text-align:left;font-family:'Oswald',sans-serif;font-size:14px;line-height:1;color:var(--ink)}
  .schedule{position:absolute;left:52px;top:1128px}
  .schedule-label{font-style:italic;font-weight:700;font-size:15px;color:var(--amber)}
  .schedule-url{margin-top:6px;font-size:19px;color:var(--white)}
</style>
</head>
<body>
<main class="flyer">
  <div class="hero-photo" role="img" aria-label="Photo of an MMA fighter throwing a high kick inside a caged arena with a crowd behind"></div>

  <svg class="backdrop" width="902" height="1200" viewBox="0 0 902 1200" aria-hidden="true">
    <path d="M0 0H902V150C720 225 420 250 0 250Z" fill="var(--silver)"/>
    <path d="M0 0H902V132C720 208 420 232 0 232Z" fill="var(--paper)"/>
    <path d="M0 0H902V120C720 195 420 218 0 218Z" fill="var(--white)"/>
    <rect x="0" y="772" width="902" height="8" fill="var(--sand-dark)"/>
    <rect x="0" y="780" width="902" height="420" fill="var(--paper)"/>
    <ellipse cx="905" cy="1165" rx="360" ry="295" fill="var(--sand)"/>
    <path d="M0 1094C240 1082 520 1110 760 1200H0Z" fill="var(--sand)"/>
    <path d="M0 1104C240 1094 510 1122 730 1200H0Z" fill="var(--ink)"/>
    <path d="M60 712H520L500 794H40Z" fill="var(--white)"/>
    <path d="M40 794H500L490 804H50Z" fill="var(--silver)"/>
  </svg>

  <header class="brand">
    <span class="brand-dot"></span>
    <span class="brand-name">aura wellness</span>
  </header>

  <div class="social">
    <span class="social-label">Follow us on :</span>
    <span class="social-square"></span>
    <span class="social-square"></span>
    <span class="social-square"></span>
    <span class="social-square"></span>
  </div>

  <section class="headline">
    <h1 class="headline-main">BOOT-CAMP</h1>
    <div class="headline-tag">FITNESS AND BOXING</div>
  </section>

  <p class="coach">With world champion<br>MMA fighter Leo<br><span class="coach-nick">“The Cobra”</span> Marsh</p>

  <p class="intro">Train and learn the techniques that made Leo a champion MMA fighter from Rhode Island and New England through this intensive but fun boot-camp class</p>

  <div class="launch">
    <p class="launch-text">COMING IN <span class="launch-month">JULY,</span> 2019</p>
  </div>

  <div class="class-photo" role="img" aria-label="Photo of a group fitness class stretching on exercise mats"></div>

  <ul class="benefits">
    <li><svg width="16" height="14" viewBox="0 0 16 14"><path d="M1 7l4 5L15 1" fill="none" stroke="var(--ink)" stroke-width="2.6"/></svg>Harbor Combat Club has partnered with Aura Wellness to offer an unparalleled metabolic, fitness and recovery program.</li>
    <li><svg width="16" height="14" viewBox="0 0 16 14"><path d="M1 7l4 5L15 1" fill="none" stroke="var(--ink)" stroke-width="2.6"/></svg>Data Driven Fitness Training</li>
    <li><svg width="16" height="14" viewBox="0 0 16 14"><path d="M1 7l4 5L15 1" fill="none" stroke="var(--ink)" stroke-width="2.6"/></svg>24/7 Remote Monitoring with Guidance of your physiological metrics through our specialized fitness track Aura Pulseband</li>
    <li><svg width="16" height="14" viewBox="0 0 16 14"><path d="M1 7l4 5L15 1" fill="none" stroke="var(--ink)" stroke-width="2.6"/></svg>Data Driven Sleep and Recovery Program</li>
    <li><svg width="16" height="14" viewBox="0 0 16 14"><path d="M1 7l4 5L15 1" fill="none" stroke="var(--ink)" stroke-width="2.6"/></svg>Personalized Dietary and Nutrition program overseen by dietary and metabolic doctors</li>
  </ul>

  <section class="pricing">
    <div class="plan">
      <span class="plan-label">Unlimited Classes:</span>
      <div class="plan-price"><span class="plan-amount">$125</span><span class="plan-unit">PER<br>MONTH</span></div>
    </div>
    <div class="plan">
      <span class="plan-label">10 Class Pass:</span>
      <div class="plan-price"><span class="plan-amount">$100</span><span class="plan-unit">PER<br>MONTH</span></div>
    </div>
    <div class="plan">
      <span class="plan-label">Drop in class:</span>
      <div class="plan-price"><span class="plan-amount">$15</span><span class="plan-unit">PER<br>MONTH</span></div>
    </div>
  </section>

  <footer class="schedule">
    <p class="schedule-label">To see Leo’s class schedule go to:</p>
    <p class="schedule-url">https://aurawellnessclub.com/class-schedule/</p>
  </footer>
</main>
</body>
</html>
```